Hadley's Labouring Service needs a logo/business cards.

i've just started a new Labouring Business, Called Hadley's Labouring Service, I provide high quality labouring servicing to local Builders and Tradesmen.
I'd like my business cards to reflect the hard work and dedication I put into my business.
I'd like to see Burnt Orange and blacks in the cards and logo.
I want my cards to catch peoples eye as there is A lot of dull business cards in my industry.

Target Market(s)

Builders and other tradesmen

Contact Information for Business Card

Hadley's Labouring Service

Font styles to use
Sans Serif

Colors
f78f20
ffc214
000000
ffffff

Requirements
Must have
• My name : Tom Hadley
• My Number: 0497563821
• Email Address : hadleylabouringservice@quoxmail.example
• A Sharp and Professional Design
Nice to have
• A unique design that separates my Cards from others,
• As I try to provide unique service to my clients I'd love my cards/logo to reflect this.

```html
<!DOCTYPE html>
<html lang="en">
<head>
<meta charset="utf-8">
<title>Hadley's Labouring Service – Business Cards</title>
<link rel="stylesheet" href="https://fonts.googleapis.com/css2?family=Oswald:wght@600&family=Roboto:wght@400&family=Roboto+Condensed:wght@700&display=swap">
<style>
  :root {
    --burnt-orange: #f78f20;
    --amber: #ffc214;
    --black: #000000;
    --card-black: #0d0d0d;
    --white: #ffffff;
    --backdrop: #2c3038;
    --faint-ring: #1d1d1d;
  }
  * { box-sizing: border-box; margin: 0; padding: 0; }
  html, body { width: 1200px; height: 900px; overflow: hidden; }
  body {
    background: var(--backdrop);
    font-family: "Roboto", sans-serif;
    position: relative;
  }
  .card {
    position: absolute;
    left: 285px;
    width: 630px;
    height: 360px;
    background: var(--card-black);
    border-radius: 4px;
    overflow: hidden;
    box-shadow: 0 14px 30px rgba(0,0,0,.45);
  }
  .card--contact { top: 50px; }
  .card--brand { top: 490px; }

  .brand-lockup {
    position: absolute;
    display: flex;
    align-items: center;
    gap: 16px;
  }
  .brand-lockup__ring {
    flex: none;
    border-radius: 50%;
    border: 5px solid var(--burnt-orange);
  }
  .brand-lockup__name {
    font-family: "Oswald", sans-serif;
    font-weight: 600;
    color: var(--burnt-orange);
    text-transform: uppercase;
    line-height: 1.02;
  }
  .brand-lockup__name span { display: block; }

  .card--contact .brand-lockup { left: 190px; top: 48px; }
  .card--contact .brand-lockup__ring { width: 70px; height: 70px; }
  .card--contact .brand-lockup__name { font-size: 34px; }
  .card--contact .brand-lockup__name span + span { font-size: 17px; letter-spacing: 1.5px; }

  .card--brand .brand-lockup { left: 50%; top: 50%; transform: translate(-50%, -50%); }
  .card--brand .brand-lockup__ring { width: 84px; height: 84px; }
  .card--brand .brand-lockup__name { font-size: 42px; }
  .card--brand .brand-lockup__name span + span { font-size: 20px; letter-spacing: 2px; }

  .faint-ring {
    position: absolute;
    right: -30px;
    bottom: -80px;
    width: 280px;
    height: 280px;
    border-radius: 50%;
    border: 16px solid var(--faint-ring);
  }

  .contact-line {
    position: absolute;
    left: 0;
    right: 40px;
    top: 186px;
    height: 34px;
    display: flex;
    align-items: flex-end;
  }
  .name-tab {
    flex: none;
    width: 190px;
    height: 34px;
    background: var(--amber);
    clip-path: polygon(0 0, 100% 0, 92% 100%, 0 100%);
    display: flex;
    align-items: center;
    gap: 10px;
    padding-left: 18px;
  }
  .name-tab__name {
    font-family: "Roboto Condensed", sans-serif;
    font-weight: 700;
    font-size: 19px;
    color: var(--black);
    text-transform: uppercase;
    letter-spacing: .5px;
    white-space: nowrap;
  }
  .rule-stripes { flex: none; display: block; }
  .email {
    flex: 1;
    min-width: 0;
    color: var(--white);
    font-size: 14px;
    white-space: nowrap;
    padding: 0 0 6px 8px;
    border-bottom: 3px solid var(--amber);
    line-height: 1.2;
  }
  .email-tab {
    flex: none;
    width: 40px;
    height: 28px;
    background: var(--amber);
    clip-path: polygon(0 0, 100% 0, 100% 100%, 18% 100%);
    display: flex;
    align-items: center;
    justify-content: center;
    padding-left: 6px;
  }
  .phone-number {
    position: absolute;
    left: 46px;
    top: 232px;
    color: var(--white);
    font-size: 16px;
    letter-spacing: .5px;
  }
</style>
</head>
<body>

  <section class="card card--contact" aria-label="Business card front">
    <div class="faint-ring" aria-hidden="true"></div>

    <div class="brand-lockup">
      <div class="brand-lockup__ring" aria-hidden="true"></div>
      <p class="brand-lockup__name"><span>Hadley's</span><span>Labouring Service</span></p>
    </div>

    <div class="contact-line">
      <div class="name-tab">
        <svg width="14" height="14" viewBox="0 0 24 24" aria-hidden="true">
          <path fill="#000" d="M6.6 10.8a15.1 15.1 0 0 0 6.6 6.6l2.2-2.2a1 1 0 0 1 1-.25 11.4 11.4 0 0 0 3.6.57 1 1 0 0 1 1 1V20a1 1 0 0 1-1 1A17 17 0 0 1 3 4a1 1 0 0 1 1-1h3.5a1 1 0 0 1 1 1c0 1.25.2 2.45.57 3.57a1 1 0 0 1-.25 1z"/>
        </svg>
        <span class="name-tab__name">Tom Hadley</span>
      </div>
      <svg class="rule-stripes" width="60" height="34" viewBox="0 0 60 34" aria-hidden="true">
        <polygon points="10,0 15,0 5,34 0,34" fill="#ffc214"/>
        <polygon points="21,0 26,0 16,34 11,34" fill="#ffc214"/>
        <polygon points="32,0 37,0 27,34 22,34" fill="#ffffff"/>
        <polygon points="43,0 48,0 38,34 33,34" fill="#ffffff"/>
        <polygon points="54,0 59,0 49,34 44,34" fill="#ffffff"/>
      </svg>
      <p class="email">hadleylabouringservice@quoxmail.example</p>
      <div class="email-tab">
        <svg width="18" height="13" viewBox="0 0 18 13" aria-hidden="true">
          <rect x="1" y="1" width="16" height="11" fill="none" stroke="#000" stroke-width="1.8"/>
          <polyline points="1,1 9,7.5 17,1" fill="none" stroke="#000" stroke-width="1.8"/>
        </svg>
      </div>
    </div>
    <p class="phone-number">0497563821</p>
  </section>

  <section class="card card--brand" aria-label="Business card back">
    <div class="brand-lockup">
      <div class="brand-lockup__ring" aria-hidden="true"></div>
      <p class="brand-lockup__name"><span>Hadley's</span><span>Labouring Service</span></p>
    </div>
  </section>

</body>
</html>
```